Packaging for Hair Extensions range

We are a successful hair extensions company who are looking at redesigning our current hair extensions packaging for a fresh and modern new look. We need a designer who is highly skilled and very modern and fashionable in their approach to design.

For this particular job need 1 piece of packaging designed but once the design is approved, we will need the design to be edited as we need it for two different product brand names. So, it will contain the same product (hair extensions) but each of the 2 packages will have different text, colours, and images.

The product is Pre Bonded hair. Please visit: http://www.velvetmuse.com.au/pre-bonded.php so you can see the product.

I have attached a document called "packaging example". this is the type of packaging we need. It will house 50cm long hair extensions. It consists of a long piece of card with a flap at the top. Unless you can think of a better way to display the hair. this link shows the hair it will contain:

http://www.lunarlockshairextensions.com.au/pd_fusion_hair_extensions_diy_kits.cfm

The two different brand names are: Velvet Muse (www.velvetmuse.com.au) and lunarlocks hair extensions (www.lunarlockshairextensions.com.au).

We also need a logo and website redesign for lunarlocks so would like to discuss that with the approved designer.

Please note:

We have many design jobs available each month as we own 3 different businesses and always need new posters, brochures, flyers, web banners and various other items designed, so the successful designer will recieve a constant stream of new work from us.

We need someone reliable who can stick to time frames as we are a fast moving company.

I look forward to seeing your design!

Target Market(s)

Women, aged between 18 and 45. Women who care about their appearance and want to look beautiful, modern, stylish and fashionable. Women who read fashion magazines and want to look like models. Women who want to be successful.

Industry/Entity Type

Lunarlocks

Requirements
Must have
• Designer must have an awareness of popular design looks and trends in the fashion, hair and beauty world.
Must be a high quality design.
We have a packaging template that needs to be adhered to.
Designer must stick to time frames.
Design needs to be high quality so designers who do not have much experience or can only produce basic designs need not apply.
For this job we will require 1 universal design but we need it for 3 different product types. So the one universal design will then need to be slightly edited to feature a different text, colour and front image. So the packaging is for hair extensions. Pack 1 is for Lunarlocks Hair Extensions and the second is for Velvet Muse Hair Extensions. This means, we use the same design but just change the product name and text and the image and colour so that the products are easily distinguished by brand name when they are up on display in a store.

The technical info is as follows:
NEW LUNARLOCKS & VELVET MUSE PACKAGING (DESIGN INFO.)

The following information relates to the NEW Lunarlocks Hair Extensions & Velvet Muse Hair Extensions Packaging:

1. Packaging DIMENSIONS: see Attachment 1 (Lunarlocks Packaging Dimensions Template).
Please note: The file to be opened and used in ‘Adobe Illustrator’. The final design likewise will be sent to us in an Adobe Illustrator file.

2. DESIGN: The packaging size will essentially be as per Attachment 2 (Old Lunarlocks Packaging Blue), but with the following changes:
• The photos, images, background and shape need to be upgraded and redesigned
• The ‘Congratulations’ statement on the rear of the packaging remains the same.
• The HAIR CARE instructions on the rear of the packet will be amended to read as follows:

- Brush hair gently using a loop brush starting at the ends and working towards the scalp while holding the top part to prevent stretching.
- Wash hair in a gentle manner in lukewarm water using a mild moisturising shampoo and conditioner. Do not scrub hair. DO NOT use shampoos and conditioners that contain Alcohol or Sodium Laureth Sulphate as these may attack the bonds on your hair extensions.
- Run fingers through hair daily to make sure the bonds are separated.
- Dry hair by wrapping in a towel or air dry. If using a blow drier use the ‘cool’ setting.
- DO NOT use hot appliances such as blow driers and hair straighteners near the bonds.
- We recommend you visit a salon every four to six weeks to have your extensions checked and readjusted to compensate for your hair growth.

3. The CONTACT information has been changed to read as follows:
LUNARLOCKS
- For customer support and queries email us at:
enquiry@lunarlockshairextensions.com.au

- For information on our range of hair extension products please visit our website:
www.lunarlockshairextensions.com.au
VELVET MUSE
wholesale@velvetmuse.com.au

www.velvetmuse.com.au

(note to designer: do not include address and phone information)

Nice to have
• Would like to see more than one choice of design
Would like to see each design in a few different colours
Should not have
• No standard fonts.
No basic designs.
I have attached an example of our current packaging. It must be better quality than this.

```html
<!DOCTYPE html>
<html lang="en">
<head>
<meta charset="utf-8">
<title>Velvet Muse Hair Extensions – Packaging</title>
<link rel="stylesheet" href="https://fonts.googleapis.com/css2?family=Jost:wght@300;400;500;600&display=swap">
<style>
  :root {
    --stage: #d9d9d9;
    --card-black: #0b0b0b;
    --band-top: #8a8580;
    --band-bottom: #5c5854;
    --text-white: #ffffff;
    --text-soft: #f1ece6;
    --accent-pink: #d62f8c;
    --blonde-light: #c7b07a;
    --blonde-mid: #8c7440;
    --blonde-dark: #3a2f1c;
    --auburn-light: #b2542c;
    --auburn-mid: #6e2a12;
    --auburn-dark: #2a0f07;
  }
  * { box-sizing: border-box; margin: 0; padding: 0; }
  html, body {
    width: 1200px; height: 900px; overflow: hidden;
    background: var(--stage);
    font-family: "Jost", "Futura", sans-serif;
  }
  .packs {
    position: relative; width: 1200px; height: 900px;
    display: flex; justify-content: center; align-items: center; gap: 70px;
  }
  .pack {
    position: relative; width: 440px; height: 840px;
    background: var(--card-black);
    padding: 0 16px 16px;
    display: flex; flex-direction: column;
  }
  .brand {
    height: 110px;
    display: flex; align-items: center; justify-content: center; gap: 12px;
  }
  .brand-mark {
    width: 14px; height: 14px; background: var(--accent-pink);
  }
  .brand-name {
    color: var(--text-white);
    font-weight: 500; font-size: 34px; letter-spacing: 1px;
    text-transform: lowercase;
  }
  .range-band {
    height: 48px; margin: 0 -16px;
    background: linear-gradient(var(--band-top), var(--band-bottom));
    display: flex; align-items: center; justify-content: center;
    color: var(--text-white); font-weight: 400; font-size: 27px;
  }
  .visual {
    position: relative; flex: 1;
    border-radius: 0 0 90px 90px;
    overflow: hidden;
    display: flex; flex-direction: column; justify-content: flex-end; align-items: center;
    padding-bottom: 60px;
  }
  .pack--blonde .visual {
    background: linear-gradient(115deg, var(--blonde-dark) 0%, var(--blonde-mid) 45%, var(--blonde-light) 70%, var(--blonde-mid) 100%);
  }
  .pack--auburn .visual {
    background: linear-gradient(100deg, var(--auburn-mid) 0%, var(--auburn-light) 35%, var(--auburn-mid) 60%, var(--auburn-dark) 100%);
  }
  .visual::after {
    content: ""; position: absolute; inset: 55% 0 0 0;
    background: linear-gradient(rgba(0,0,0,0), rgba(0,0,0,0.55));
  }
  .claim {
    position: relative; z-index: 1;
    color: var(--text-soft); font-weight: 300; font-size: 25px;
  }
  .product {
    position: relative; z-index: 1;
    color: var(--text-white); font-weight: 600; font-size: 42px; letter-spacing: 1px;
    margin-top: 2px;
  }
</style>
</head>
<body>
  <main class="packs">
    <section class="pack pack--blonde">
      <header class="brand">
        <span class="brand-mark"></span>
        <span class="brand-name">velvet muse</span>
      </header>
      <div class="range-band">Hair Extensions</div>
      <div class="visual" role="img" aria-label="Photo of a model with long blonde hair falling across her face">
        <p class="claim">100% Diamond Remy</p>
        <p class="product">HUMAN HAIIR</p>
      </div>
    </section>

    <section class="pack pack--auburn">
      <header class="brand">
        <span class="brand-mark"></span>
        <span class="brand-name">velvet muse</span>
      </header>
      <div class="range-band">Hair Extensions</div>
      <div class="visual" role="img" aria-label="Photo of a model with long straight auburn hair covering half her face">
        <p class="claim">100% Diamond Remy</p>
        <p class="product">HUMAN HAIIR</p>
      </div>
    </section>
  </main>
</body>
</html>
```